Roofing Company Modern look

I want a modern and sophisticated look for our roofing business.

Our address is :

5172 Maple Crane Rd
Orlando, Fl 32825

(407)-555-2719

www.SummitPeakRoofs.example

I also want to make sure on the back there is a spot to put
Project Manager Name :

Number:

Because the cards will be used by all sales people

Project Manager Name :

Also there are accreditation we have logos are uploaded here as well that I would like maybe on the back of card as well

I also want to highlight our special attributions or trades:

Residential & Commercial
Fully Insured
License # CCC8274916
Insurance Claims
Serving Central Florida Since 1992
Free Estimates

Contact Information for Business Card

Our address is :

5172 Maple Crane Rd
Orlando, Fl 32825

(407)-555-2719

Project Manager Name :

Residential & Commercial
Fully Insured
License # CCC8274916
Insurance Claims
Free Estimates

Font styles to use
Serif
Sans Serif

Colors
3176b5

Requirements
Must have
• Must have royal blue like my logo grey and black are the colors I like

```html
<!DOCTYPE html>
<html lang="en">
<head>
<meta charset="utf-8">
<title>Summit Peak Roofing & Gutters – Business Card</title>
<link rel="stylesheet" href="https://fonts.googleapis.com/css2?family=Montserrat:wght@500;600;700;800&family=Poppins:wght@400;500;600&display=swap">
<style>
  :root {
    --royal: #3176b5;
    --royal-deep: #1f5f9f;
    --royal-light: #4f95d3;
    --ink: #1b1b1d;
    --grey: #6d6f73;
    --paper: #ffffff;
    --backdrop: #e7e9ec;
    --badge-red: #c8202a;
    --badge-navy: #233a6a;
  }
  * { margin: 0; padding: 0; box-sizing: border-box; }
  html, body { width: 1200px; height: 800px; overflow: hidden; }
  body {
    background: var(--backdrop);
    font-family: "Poppins", sans-serif;
    color: var(--ink);
    position: relative;
  }
  .card {
    position: absolute;
    width: 560px;
    height: 320px;
    background: var(--paper);
    border-radius: 18px;
    overflow: hidden;
    box-shadow: 0 10px 30px rgba(0,0,0,.15);
    top: 240px;
  }
  .card--front { left: 27px; }
  .card--back { left: 613px; }

  /* Brand name stand-in */
  .brand { display: flex; align-items: center; gap: 12px; }
  .brand__dot { width: 40px; height: 40px; border-radius: 50%; background: var(--royal); flex: none; }
  .brand__name {
    font-family: "Montserrat", sans-serif;
    font-weight: 700;
    color: var(--royal);
    letter-spacing: 3px;
    line-height: 1.1;
  }
  .brand__name span { display: block; }
  .brand__name .brand__sub { font-size: 0.42em; letter-spacing: 2px; }

  /* Front */
  .card--front .brand { position: absolute; left: 110px; top: 80px; }
  .card--front .brand__name { font-size: 40px; }
  .badges { position: absolute; left: 0; right: 0; top: 200px; display: flex; justify-content: center; align-items: center; gap: 26px; }
  .badge { flex: none; }
  .badge--hex { width: 70px; height: 46px; background: var(--badge-navy); clip-path: polygon(15% 0,85% 0,100% 50%,85% 100%,15% 100%,0 50%); }
  .badge--banner { width: 140px; height: 40px; background: var(--badge-red); border: 3px solid var(--badge-navy); }
  .badge--seal { width: 52px; height: 52px; border-radius: 50%; background: #e9eef0; border: 4px solid #5e9a8a; }
  .badge--shield { width: 40px; height: 50px; background: var(--royal-deep); border-radius: 4px 4px 20px 20px; }

  /* Back */
  .back-curve { position: absolute; inset: 0; }
  .contact-person {
    position: absolute; right: 30px; top: 24px; text-align: right; color: #fff;
  }
  .contact-person__name { font-family: "Montserrat", sans-serif; font-weight: 600; font-size: 26px; letter-spacing: 2px; }
  .contact-person__title { font-family: "Montserrat", sans-serif; font-weight: 500; font-size: 14px; letter-spacing: 1.5px; }
  .contact-person__phone { font-weight: 600; font-size: 14px; letter-spacing: 1px; }

  .card--back .brand { position: absolute; left: 24px; top: 98px; gap: 8px; }
  .card--back .brand__dot { width: 28px; height: 28px; }
  .card--back .brand__name { font-size: 22px; letter-spacing: 2px; }

  .contact-list { position: absolute; left: 26px; top: 168px; list-style: none; font-size: 13px; line-height: 20px; }
  .contact-list li { display: flex; align-items: center; gap: 8px; }
  .contact-list svg { width: 13px; height: 13px; fill: var(--royal); flex: none; }
  .license { position: absolute; left: 26px; top: 240px; color: var(--royal); font-size: 14px; }

  .address { position: absolute; right: 30px; top: 132px; text-align: right; font-size: 13px; line-height: 19px; display: flex; gap: 8px; }
  .address svg { width: 14px; height: 18px; fill: var(--royal); }

  .offers { position: absolute; right: 30px; top: 196px; display: flex; align-items: center; gap: 18px; }
  .offer-free { display: flex; align-items: center; gap: 8px; }
  .offer-free svg { width: 30px; height: 30px; }
  .offer-free__text { font-family: "Montserrat", sans-serif; font-weight: 800; color: var(--royal); line-height: 1; }
  .offer-free__big { font-size: 26px; display: block; }
  .offer-free__small { font-size: 10px; letter-spacing: 0.5px; }
  .since { font-family: "Montserrat", sans-serif; font-weight: 800; color: var(--royal); line-height: 1.05; font-size: 15px; }
  .since small { display: block; font-size: 8px; }

  .service-band {
    position: absolute; left: 0; right: 0; bottom: 0; height: 46px;
    background: linear-gradient(90deg, var(--royal-deep), var(--royal-light));
    display: flex; align-items: center; justify-content: space-around; color: #fff; font-size: 14px;
  }
  .service-band__item { display: flex; align-items: center; gap: 8px; }
  .service-band svg { width: 18px; height: 18px; fill: #fff; }
</style>
</head>
<body>

  <section class="card card--front" aria-label="Card front">
    <div class="brand">
      <div class="brand__dot"></div>
      <div class="brand__name"><span>SUMMIT PEAK</span><span class="brand__sub">ROOFING &amp; GUTTERS INC.</span></div>
    </div>
    <div class="badges">
      <div class="badge badge--hex" role="img" aria-label="Shingle applicator certification badge"></div>
      <div class="badge badge--banner" role="img" aria-label="Authorized roofing contractor badge"></div>
      <div class="badge badge--seal" role="img" aria-label="Screened and approved listing seal"></div>
      <div class="badge badge--shield" role="img" aria-label="Accredited business rating badge"></div>
    </div>
  </section>

  <section class="card card--back" aria-label="Card back">
    <svg class="back-curve" viewBox="0 0 560 320" preserveAspectRatio="none" aria-hidden="true">
      <defs>
        <linearGradient id="curveFill" x1="0" y1="1" x2="1" y2="0">
          <stop offset="0" stop-color="#1f5f9f"/>
          <stop offset="1" stop-color="#4f95d3"/>
        </linearGradient>
      </defs>
      <path d="M150 0 H560 V105 C470 120 320 118 150 0 Z" fill="url(#curveFill)"/>
    </svg>

    <div class="contact-person">
      <div class="contact-person__name">ALEX MORGAN</div>
      <div class="contact-person__title">PROJECT MANAGER</div>
      <div class="contact-person__phone">0123-555-0198</div>
    </div>

    <div class="brand">
      <div class="brand__dot"></div>
      <div class="brand__name"><span>SUMMIT PEAK</span><span class="brand__sub">ROOFING &amp; GUTTERS INC.</span></div>
    </div>

    <ul class="contact-list">
      <li><svg viewBox="0 0 24 24"><path d="M6.6 10.8a15 15 0 0 0 6.6 6.6l2.2-2.2a1 1 0 0 1 1-.25 11.4 11.4 0 0 0 3.6.57 1 1 0 0 1 1 1V20a1 1 0 0 1-1 1A17 17 0 0 1 3 4a1 1 0 0 1 1-1h3.5a1 1 0 0 1 1 1c0 1.25.2 2.45.57 3.57a1 1 0 0 1-.25 1z"/></svg>(407)-555-2719</li>
      <li><svg viewBox="0 0 24 24"><path d="M2 5h20v14H2z M4 7v.4l8 5 8-5V7l-8 5z" fill-rule="evenodd"/></svg>info@SummitPeakRoofs.example</li>
      <li><svg viewBox="0 0 24 24"><path d="M12 2a10 10 0 1 0 0 20 10 10 0 0 0 0-20zm0 2c.9 1.2 1.6 2.6 2 4h-4c.4-1.4 1.1-2.8 2-4zM4.3 14a8 8 0 0 1 0-4h3.4a16 16 0 0 0 0 4zm5.7 0a14 14 0 0 1 0-4h4a14 14 0 0 1 0 4zm6.3 0a16 16 0 0 0 0-4h3.4a8 8 0 0 1 0 4z"/></svg>www.SummitPeakRoofs.example</li>
    </ul>
    <div class="license">License # CCC8274916</div>

    <div class="address">
      <div>5172 Maple Crane Rd<br>Orlando, Fl 32825</div>
      <svg viewBox="0 0 24 30"><path d="M12 0a10 10 0 0 0-10 10c0 7.5 10 20 10 20s10-12.5 10-20A10 10 0 0 0 12 0zm0 14a4 4 0 1 1 0-8 4 4 0 0 1 0 8z"/></svg>
    </div>

    <div class="offers">
      <div class="offer-free">
        <svg viewBox="0 0 30 30"><circle cx="15" cy="15" r="13" fill="#3176b5"/><circle cx="15" cy="15" r="10" fill="#fff"/><path d="M10 15l4 4 7-8" stroke="#1b1b1d" stroke-width="2.5" fill="none"/></svg>
        <div class="offer-free__text"><span class="offer-free__big">FREE</span><span class="offer-free__small">ESTIMATES!</span></div>
      </div>
      <div class="since">SERVING<small>CENTRAL FLORIDA</small>SINCE 1992</div>
    </div>

    <div class="service-band">
      <div class="service-band__item"><svg viewBox="0 0 24 24"><path d="M3 11l6-5 6 5v10H3zM13 3h8v18h-4V11z"/></svg>Residential &amp; Commercial</div>
      <div class="service-band__item"><svg viewBox="0 0 24 24"><path d="M12 2A10 10 0 0 0 2 12h9v7a2 2 0 0 1-4 0h-2a4 4 0 0 0 8 0v-7h9A10 10 0 0 0 12 2z"/></svg>Fully Insured</div>
      <div class="service-band__item"><svg viewBox="0 0 24 24"><path d="M5 2h10l4 4v16H5zM8 9h8v2H8zm0 4h8v2H8zm0 4h5v2H8z"/></svg>Insurance Claims</div>
    </div>
  </section>

</body>
</html>
```